Website re-design

We are a successful furnished apartment provider in Boston. We currently are working on re-designing our website www.ribtenlofts.com to make it more modern, designer look and user friendly. We hired a designer, but are not happy with the designs proposed and want to improve on them. The winning design will be paid regardless of whether we stay with our current designer or not. We want ideas and functional page links to see how it will work. Platform we have chosen is wordpress. Feel free to propose others easy for us to update and modify. We do not like Joomla on which website is currently running. We do not like flash nor long load times.
Please use photos on our website for design presentations. www.ribtenlofts.com

Target Market(s)

doctors, nurses, business men but mostly business women, some post-medical students

Industry/Entity Type

Apartment

Requirements
Must have
• Quick action button for reservation form and a notification and email forwarding system to us of reservation information by potential clients. Blog required with feedback by guests allowed, we can censor which are published. Slide shows of apartments.
Should not have
• No movies.

```html
<!DOCTYPE html>
<html lang="en">
<head>
<meta charset="utf-8">
<title>Ribten Lofts – Furnished Apartments</title>
<link href="https://fonts.googleapis.com/css2?family=Cinzel:wght@400;600;700&family=PT+Sans:wght@400;700&display=swap" rel="stylesheet">
<style>
  :root {
    --bg-top: #c9bf85;
    --bg-bottom: #ebe5d3;
    --header-black: #0b0a09;
    --gold: #c9b27a;
    --gold-soft: #b8a676;
    --nav-band: rgba(120, 104, 78, 0.72);
    --nav-text: #ead3a4;
    --nav-active: #ffffff;
    --panel: #ffffff;
    --frame: #d8d2c4;
    --heading: #776744;
    --body-text: #7a6a48;
    --link-text: #2b2319;
    --footer-text: #b5a686;
    --social: #5a5650;
  }
  * { margin: 0; padding: 0; box-sizing: border-box; }
  html, body { width: 1200px; height: 1001px; overflow: hidden; }
  body {
    background: linear-gradient(to bottom, var(--bg-top) 0%, #d8d0a6 40%, var(--bg-bottom) 100%);
    font-family: "PT Sans", sans-serif;
    position: relative;
  }
  .site-header {
    position: absolute; left: 240px; top: 53px; width: 721px; height: 98px;
    background: var(--header-black);
  }
  .brand { position: absolute; left: 34px; top: 26px; display: flex; align-items: center; gap: 10px; }
  .brand-mark { width: 46px; height: 46px; border-radius: 50%; background: var(--gold); }
  .brand-name { font-family: "Cinzel", serif; font-weight: 400; font-size: 23px; color: var(--gold); letter-spacing: 1px; line-height: 1; }
  .brand-tag { font-family: "Cinzel", serif; font-size: 8px; color: var(--gold); letter-spacing: 2px; margin-top: 3px; }
  .utility-nav { position: absolute; left: 336px; top: 52px; display: flex; gap: 15px; }
  .utility-nav a { font-family: "Cinzel", serif; font-size: 11px; color: var(--gold-soft); text-decoration: none; }
  .social { position: absolute; left: 634px; top: 52px; display: flex; gap: 7px; }
  .social span { width: 12px; height: 12px; background: var(--social); display: block; }

  .gallery {
    position: absolute; left: 247px; top: 518px; width: 706px; height: 158px;
    background: var(--panel);
  }
  .hero-shadow {
    position: absolute; left: 267px; top: 508px; width: 667px; height: 10px;
    box-shadow: 0 4px 7px rgba(0,0,0,0.45); background: transparent;
  }
  .hero {
    position: absolute; left: 240px; top: 151px; width: 721px; height: 367px;
    background:
      radial-gradient(ellipse at 55% 55%, #f1ece3 0%, rgba(241,236,227,0) 28%),
      radial-gradient(ellipse at 92% 90%, #a8231d 0%, rgba(168,35,29,0) 30%),
      linear-gradient(160deg, #c9702c 0%, #d78a45 35%, #9b5a2c 70%, #6f3f1e 100%);
  }
  .main-nav {
    position: absolute; left: 240px; top: 151px; width: 721px; height: 41px;
    background: var(--nav-band);
  }
  .main-nav a {
    position: absolute; top: 13px; font-family: "Cinzel", serif; font-size: 14px;
    color: var(--nav-text); text-decoration: none;
  }
  .main-nav a.is-active { color: var(--nav-active); font-weight: 700; }
  .thumb {
    position: absolute; top: 19px; width: 160px; height: 116px;
    border: 1px solid var(--frame); padding: 3px; background: #fff;
  }
  .thumb-photo { width: 100%; height: 100%; position: relative; }
  .thumb-label {
    position: absolute; left: 0; right: 0; bottom: 0; height: 41px;
    background: rgba(40, 28, 18, 0.6);
    font-family: "Cinzel", serif; font-weight: 700; font-size: 13px; color: #e6cf92;
    display: flex; align-items: center; justify-content: center;
  }
  .listing { position: absolute; left: 240px; top: 720px; width: 721px; text-align: center; }
  .listing h1 { font-family: "Cinzel", serif; font-weight: 400; font-size: 14.5px; color: var(--heading); letter-spacing: 0.4px; }
  .listing p { font-size: 10px; font-weight: 700; color: var(--body-text); line-height: 15.5px; }
  .details { margin-top: 12px; }
  .stay { margin-top: 17px; }
  .actions { margin-top: 34px; font-size: 10px; font-weight: 700; color: var(--link-text); }
  .actions a { color: var(--link-text); text-decoration: none; }
  .site-footer {
    position: absolute; left: 240px; top: 948px; width: 721px; text-align: center;
    font-family: "Cinzel", serif; font-size: 9px; color: var(--footer-text);
  }
</style>
</head>
<body>
  <header class="site-header">
    <div class="brand">
      <span class="brand-mark"></span>
      <div>
        <div class="brand-name">RIBTEN LOFTS</div>
        <div class="brand-tag">FURNISHED APARTMENTS</div>
      </div>
    </div>
    <nav class="utility-nav">
      <a href="#">Blog</a><a href="#">News</a><a href="#">Reviews</a><a href="#">Boston</a><a href="#">About Us</a>
    </nav>
    <div class="social"><span></span><span></span><span></span></div>
  </header>

  <section class="gallery">
    <div class="thumb" style="left:20px">
      <div class="thumb-photo" role="img" aria-label="Living area with bed" style="background:linear-gradient(150deg,#c98a4a,#8a5a30)">
        <div class="thumb-label">Living Area</div></div></div>
    <div class="thumb" style="left:189px">
      <div class="thumb-photo" role="img" aria-label="Kitchen with counter" style="background:linear-gradient(150deg,#d4965c,#7a4e2e)">
        <div class="thumb-label">Kitchen</div></div></div>
    <div class="thumb" style="left:358px">
      <div class="thumb-photo" role="img" aria-label="Writing area with desk by window" style="background:linear-gradient(150deg,#c07a48,#6e4428)">
        <div class="thumb-label">Writing Area</div></div></div>
    <div class="thumb" style="left:526px">
      <div class="thumb-photo" role="img" aria-label="Bright room with windows" style="background:linear-gradient(150deg,#e2b27a,#a06c3c)">
        <div class="thumb-label">Other</div></div></div>
  </section>
  <div class="hero-shadow"></div>

  <div class="hero" role="img" aria-label="Furnished studio apartment with bed, armchair, red sofa and wall TV"></div>
  <nav class="main-nav">
    <a href="#" style="left:74px">Contact</a>
    <a href="#" class="is-active" style="left:174px">Apartments</a>
    <a href="#" style="left:294px">Reservations</a>
    <a href="#" style="left:422px">Links</a>
    <a href="#" style="left:500px">Locations</a>
    <a href="#" style="left:611px">Rates</a>
  </nav>

  <main class="listing">
    <h1>Corporate Housing and Furnished Apartment 5W - Ribten Guest House</h1>
    <div class="details">
      <p>Alder Street Location Our Corporate Housing value:</p>
      <p>Queen size bed, 450 square feet, wireless DSL, Cable TV service included, A/C,</p>
      <p>BATHTUB, flat screen TV, beautiful kitchen with eat in counter.</p>
    </div>
    <div class="stay">
      <p>Minimum stay 4 weeks:</p>
      <p>rear of property on quiet side</p>
    </div>
    <div class="actions"><a href="#">Rates</a> &nbsp;|&nbsp; <a href="#">Make Reservation Request</a></div>
  </main>

  <footer class="site-footer">© Ribten Lofts 2012 - All Rights Reserved</footer>
</body>
</html>
```